Bluebird Listings ad 2014 15

I need a design for an advertisement in our Bluebird Listings book telephone directory.
The directory runs for a 12 month period.

Our business offers 24 hour glass replacements to homes, shops and offices.
Our service is usually required by customers that require their glass replaced urgently
.
The ad is 1 of many in the directory offering the same service so we need to attract the customers attention quickly and easily and deliver our message - "24hr glass replacements to doors windows and shopfronts. Call now 9372 4816".

I want to keep the data in the attached ad but with a professional graphic presentation.

The ad size is 58mm high x 83mm wide, full colour.

Target Market(s)

Our customer is generally someone in need of an emergency repair. They aren't spending time shopping around for a product, they have a problem that they want fixed promptly and professionally.

Industry/Entity Type

Business

Font styles to use
Sans Serif

Colors
0255a3
f37022

Requirements
Must have
• "24HR" must stand out, this is a key aspect of our service. The ad needs to be clear and easy to read.

```html
<!DOCTYPE html>
<html lang="en">
<head>
<meta charset="utf-8">
<title>Steadfast Glass – 24HR Glass Replacement</title>
<link rel="stylesheet" href="https://fonts.googleapis.com/css2?family=Archivo+Black&family=Archivo:wght@700&display=swap">
<style>
  :root {
    --brand-blue: #0255a3;
    --brand-blue-deep: #01407d;
    --brand-orange: #f37022;
    --crack-light: #7fa9d6;
    --photo-grey: #8a8f8c;
    --photo-brick: #9a4a3a;
    --photo-dark: #3c4440;
  }
  * { box-sizing: border-box; margin: 0; padding: 0; }
  html, body { width: 1200px; height: 900px; overflow: hidden; background: var(--brand-blue); }
  .ad {
    position: relative; width: 1200px; height: 900px; overflow: hidden;
    background: var(--brand-blue);
    font-family: "Archivo Black", "Arial Black", sans-serif;
    color: var(--brand-orange);
  }
  .ad__backdrop {
    position: absolute; left: 0; top: 250px; width: 1200px; height: 650px;
    background: radial-gradient(ellipse at 520px 210px, var(--crack-light) 0%, var(--brand-blue) 38%, var(--brand-blue-deep) 100%);
  }
  .headline {
    position: absolute; left: 0; width: 1200px; text-align: center;
    font-weight: 400; line-height: 1; white-space: nowrap;
  }
  .headline--top { top: 26px; font-size: 74px; letter-spacing: 0.3em; padding-left: 0.3em; }
  .headline--fix { top: 262px; font-size: 74px; letter-spacing: 0.36em; padding-left: 0.36em; }
  .photo-strip { position: absolute; left: 0; top: 120px; width: 1200px; height: 130px; display: flex; }
  .photo-strip__item { height: 100%; }
  .photo-strip__item--door { width: 385px; background: linear-gradient(135deg, var(--photo-grey), #5f7a70); }
  .photo-strip__item--window { width: 335px; background: linear-gradient(180deg, #d8d8d0, var(--photo-dark)); }
  .photo-strip__item--house { width: 260px; background: linear-gradient(90deg, var(--photo-brick), #2c3338 50%, var(--photo-brick)); }
  .photo-strip__item--shop { width: 220px; background: linear-gradient(135deg, #4b5a52, #9aa6a0); }
  .badge-24hr {
    position: absolute; left: 5px; top: 375px; width: 415px; height: 197px;
    background: var(--brand-orange); border-radius: 10px;
    display: flex; align-items: center; justify-content: center;
    color: var(--brand-blue); font-size: 108px; letter-spacing: 0.06em; padding-left: 0.06em;
  }
  .service-list { position: absolute; right: 5px; top: 368px; list-style: none; }
  .service-list__item {
    display: flex; align-items: center; justify-content: flex-end;
    height: 72px; font-size: 46px; white-space: nowrap;
  }
  .service-list__tick { width: 88px; height: 66px; margin-left: 8px; flex: none; }
  .brand-name {
    position: absolute; left: 0; top: 652px; width: 1200px; text-align: center;
    font-size: 100px; line-height: 1.1; white-space: nowrap;
  }
  .tagline {
    position: absolute; right: 20px; top: 778px;
    font-family: "Archivo", "Arial", sans-serif; font-weight: 700;
    font-size: 40px; line-height: 1; white-space: nowrap;
  }
  .call-now {
    position: absolute; left: 0; top: 832px; width: 1200px; text-align: center;
    font-size: 50px; line-height: 1; letter-spacing: 0.04em; white-space: nowrap;
  }
</style>
</head>
<body>
<main class="ad">
  <div class="ad__backdrop" role="img" aria-label="Shattered glass with cracks radiating from a central impact point"></div>

  <h1 class="headline headline--top">BROKEN GLASS?</h1>

  <div class="photo-strip">
    <div class="photo-strip__item photo-strip__item--door" role="img" aria-label="Shattered glass door panel"></div>
    <div class="photo-strip__item photo-strip__item--window" role="img" aria-label="Broken window pane with a large hole"></div>
    <div class="photo-strip__item photo-strip__item--house" role="img" aria-label="Broken window in a brick house wall"></div>
    <div class="photo-strip__item photo-strip__item--shop" role="img" aria-label="Smashed shopfront glass"></div>
  </div>

  <h2 class="headline headline--fix">WE CAN FIX IT</h2>

  <div class="badge-24hr">24HR</div>

  <ul class="service-list">
    <li class="service-list__item">DOOR GLASS
      <svg class="service-list__tick" viewBox="0 0 92 70" aria-hidden="true"><path d="M4 38 L20 28 L36 48 L82 2 L90 12 L36 68 Z" fill="var(--brand-orange)"/></svg></li>
    <li class="service-list__item">WINDOW GLASS
      <svg class="service-list__tick" viewBox="0 0 92 70" aria-hidden="true"><path d="M4 38 L20 28 L36 48 L82 2 L90 12 L36 68 Z" fill="var(--brand-orange)"/></svg></li>
    <li class="service-list__item">SHOWER GLASS
      <svg class="service-list__tick" viewBox="0 0 92 70" aria-hidden="true"><path d="M4 38 L20 28 L36 48 L82 2 L90 12 L36 68 Z" fill="var(--brand-orange)"/></svg></li>
    <li class="service-list__item">SHOPFRONT GLASS
      <svg class="service-list__tick" viewBox="0 0 92 70" aria-hidden="true"><path d="M4 38 L20 28 L36 48 L82 2 L90 12 L36 68 Z" fill="var(--brand-orange)"/></svg></li>
  </ul>

  <p class="brand-name">Steadfast Glass</p>
  <p class="tagline">The trusted name in glass replacement</p>
  <p class="call-now">CALL NOW 9372 4816</p>
</main>
</body>
</html>
```